Bottle label design for a mulberry brandy

Please create a label design for a mulberry brandy. The registered brand name is "Kolvat"
The brandy will be produced in Armenia from 100% mulberry.
Color of the product: transparent.
The product will be sold worldwide. The price will be between 30 and 50 USD. So the product will be in premium category.
Therefore we need a solid design, appropriate to the product price category. The design, however, needs to be modern and optimistic.
You can have mulberries on the label or not have, it is up to you.
We have chosen for the product some bottle types, the links to the available bottles you can find in the attachment. Ideally you show a picture of your label on the bottle you selected.

Target Market(s)

worldwide

```html
<!DOCTYPE html>
<html lang="en">
<head>
<meta charset="utf-8">
<title>Kolvat Mulberry Brandy — Label</title>
<link rel="stylesheet" href="https://fonts.googleapis.com/css2?family=Cinzel:wght@400;500&family=Great+Vibes&family=Josefin+Sans:wght@300;400;600&display=swap">
<style>
  :root {
    --gold: #f5c400;
    --gold-soft: #b8931a;
    --label-black: #14130e;
    --ink-white: #ffffff;
    --page: #ffffff;
    --leaf: #6fa834;
    --berry: #4a2a4d;
  }
  * { margin: 0; padding: 0; box-sizing: border-box; }
  html, body {
    width: 1029px; height: 1200px; overflow: hidden;
    background: var(--page);
  }
  .canvas { position: relative; width: 1029px; height: 1200px; }

  /* Neck label */
  .neck-label {
    position: absolute; left: 401px; top: 30px;
    width: 227px; height: 233px;
    background: var(--label-black);
  }
  .neck-label .band {
    position: absolute; left: 0; width: 100%; height: 14px; background: var(--gold);
  }
  .neck-label .band--top { top: 10px; }
  .neck-label .band--bottom { bottom: 10px; }
  .neck-label .brand {
    position: absolute; top: 62px; width: 100%; text-align: center;
    font-family: 'Cinzel', serif; font-size: 52px; color: var(--gold);
    line-height: 1;
  }
  .neck-label .age {
    position: absolute; top: 128px; width: 100%; text-align: center;
    color: var(--ink-white); line-height: 1;
  }
  .neck-label .age .script { font-size: 24px; }
  .neck-label .age .num { font-size: 42px; }

  /* Main label */
  .main-label {
    position: absolute; left: 260px; top: 282px;
    width: 510px; height: 910px;
  }
  .main-label .shape { position: absolute; inset: 0; }
  .main-label .line { position: absolute; left: 0; width: 100%; text-align: center; line-height: 1; }

  .fruit-art {
    position: absolute; left: 100px; top: 78px; width: 320px; height: 320px;
    border-radius: 50%;
    background: radial-gradient(circle at 55% 55%, var(--berry) 0 18%, var(--leaf) 40%, rgba(111,168,52,0.35) 62%, rgba(20,19,14,0) 72%);
  }

  .brand-name {
    top: 418px; font-family: 'Cinzel', serif; font-weight: 400;
    font-size: 104px; color: var(--gold); letter-spacing: 1px;
  }
  .variety {
    top: 530px; font-family: 'Great Vibes', cursive; font-size: 78px; color: var(--gold);
  }
  .category {
    top: 628px; font-family: 'Josefin Sans', sans-serif; font-weight: 600;
    font-size: 24px; letter-spacing: 6px; color: var(--ink-white);
  }
  .age { color: var(--ink-white); }
  .main-label .age { top: 680px; }
  .script { font-family: 'Great Vibes', cursive; font-size: 36px; }
  .num {
    font-family: 'Josefin Sans', sans-serif; font-weight: 300;
    font-size: 64px; color: var(--gold); margin: 0 10px; vertical-align: -6px;
  }
  .origin {
    top: 782px; font-family: 'Josefin Sans', sans-serif; font-weight: 600;
    font-size: 15px; letter-spacing: 4px; color: var(--ink-white);
  }
  .specs {
    position: absolute; top: 826px; left: 92px; right: 92px;
    display: flex; justify-content: space-between; align-items: baseline;
    font-family: 'Josefin Sans', sans-serif; font-weight: 600; color: var(--ink-white);
  }
  .specs .value { font-size: 27px; }
  .specs .unit { font-size: 17px; font-weight: 400; margin-left: 6px; }
</style>
</head>
<body>
<div class="canvas">

  <div class="neck-label">
    <div class="band band--top"></div>
    <div class="brand">Kolvat</div>
    <div class="age"><span class="script">Aged</span><span class="num" style="font-size:40px;margin:0 6px;">5</span><span class="script">years</span></div>
    <div class="band band--bottom"></div>
  </div>

  <div class="main-label">
    <svg class="shape" width="510" height="910" viewBox="0 0 510 910" aria-hidden="true">
      <path d="M0,36 Q255,-24 510,36 L471,910 L39,910 Z" fill="var(--label-black)"/>
      <path d="M19,58 Q255,4 491,58 L455,888 L55,888 Z" fill="none" stroke="var(--gold)" stroke-width="6"/>
      <path d="M34,72 Q255,22 476,72 L442,874 L68,874 Z" fill="none" stroke="var(--gold-soft)" stroke-width="1.5"/>
    </svg>

    <div class="fruit-art" role="img" aria-label="Illustration of a mulberry branch with green leaves and two dark ripe mulberries"></div>

    <div class="line brand-name">Kolvat</div>
    <div class="line variety">Mullberry</div>
    <div class="line category">BRANDY</div>
    <div class="line age"><span class="script">Aged</span><span class="num">5</span><span class="script">years</span></div>
    <div class="line origin">MADE IN ARMENIA</div>
    <div class="specs">
      <span><span class="value">51%</span><span class="unit">ALC/VOL</span></span>
      <span><span class="value">750</span><span class="unit">ML</span></span>
    </div>
  </div>

</div>
</body>
</html>
```